Anzeigengestaltung für Online-Handel mit Edelmetallen
Zielgruppe
Online Handel mit Edelmetallen wie Gold und Silberbarren und Münzen.
Sowie der Ankauf von Gold per Postankauf
Aufgabenstellung
Ich möchte in verschiedenen Tageszeitungen in Deutschland Werbung schalten . Kleine Anzeigen etwas kleiner als Visitenkarten Größe wegen den Kosten.
Logo
Ihr Onlineshop für Edelmetalle
Vergleichen sie unsere Preis
Goldbarren / Falkenthaler
Shop.Wertkontorlo.de

```html
<!DOCTYPE html>
<html lang="de">
<head>
<meta charset="utf-8">
<title>Wertkontor-Lo – Anzeige Edelmetalle</title>
<link rel="stylesheet" href="https://fonts.googleapis.com/css2?family=Bebas+Neue&family=Philosopher:wght@400;700&family=Poppins:wght@500&display=swap">
<style>
  :root {
    --page: #efeeee;
    --charcoal: #38383a;
    --gold: #d0a04a;
    --white: #ffffff;
    --photo-dark: #4a3a1c;
    --photo-mid: #a8731c;
    --photo-light: #f2c04a;
  }
  * { margin: 0; padding: 0; box-sizing: border-box; }
  html, body {
    width: 1200px; height: 1200px; overflow: hidden;
    background: var(--page);
  }
  .ad {
    position: absolute; left: 50px; top: 134px;
    width: 1100px; height: 932px;
    background: var(--charcoal);
    overflow: hidden;
  }
  .ad__art { position: absolute; inset: 0; }
  .ad__headline {
    position: absolute; left: 0; right: 0; top: 70px;
    text-align: center;
    font-family: "Philosopher", serif; font-weight: 700;
    font-size: 68px; color: var(--white);
    letter-spacing: 0.5px;
  }
  .price-badge {
    position: absolute; left: 60px; top: 274px;
    width: 384px; height: 384px; border-radius: 50%;
    background: var(--gold);
    box-shadow: 0 18px 40px rgba(0,0,0,0.35);
    display: flex; align-items: center; justify-content: center;
  }
  .price-badge::before {
    content: ""; position: absolute; inset: 16px;
    border: 4px solid var(--white); border-radius: 50%;
  }
  .price-badge__text {
    font-family: "Bebas Neue", sans-serif;
    font-size: 58px; line-height: 1.12;
    color: var(--white); text-align: center;
    transform: rotate(4deg);
  }
  .brand-name {
    position: absolute; left: 43px; width: 400px; top: 818px;
    text-align: center;
    font-family: "Philosopher", serif; font-weight: 400;
    font-size: 36px; color: var(--white);
  }
  .shop-button {
    position: absolute; left: 487px; top: 756px;
    width: 587px; height: 77px; border-radius: 14px;
    background: var(--gold);
    display: flex; align-items: center; justify-content: center;
    font-family: "Poppins", sans-serif; font-weight: 500;
    font-size: 37px; color: var(--white);
  }
</style>
</head>
<body>
  <div class="ad">
    <svg class="ad__art" width="1100" height="932" viewBox="0 0 1100 932">
      <defs>
        <linearGradient id="photoBase" x1="0" y1="0" x2="1" y2="0.4">
          <stop offset="0" stop-color="#3e3628"/>
          <stop offset="0.45" stop-color="#8a6424"/>
          <stop offset="1" stop-color="#d39a2c"/>
        </linearGradient>
        <radialGradient id="photoGlow" cx="0.68" cy="0.62" r="0.5">
          <stop offset="0" stop-color="#f7d46a" stop-opacity="0.95"/>
          <stop offset="0.6" stop-color="#d79a2a" stop-opacity="0.5"/>
          <stop offset="1" stop-color="#d79a2a" stop-opacity="0"/>
        </radialGradient>
      </defs>
      <g role="img" aria-label="Foto: Goldbarren und Goldmünzen in warmem, funkelndem Licht">
        <path d="M0,0 H1100 V604 Q560,730 0,569 Z" fill="url(#photoBase)"/>
        <path d="M0,0 H1100 V604 Q560,730 0,569 Z" fill="url(#photoGlow)"/>
      </g>
      <path d="M0,569 Q560,730 1100,604" fill="none" stroke="var(--gold)" stroke-width="6"/>
    </svg>

    <h1 class="ad__headline">Ihr Onlineshop für Edelmetalle</h1>

    <div class="price-badge">
      <p class="price-badge__text">Vergleichen<br>Sie unsere<br>Preis!</p>
    </div>

    <p class="brand-name">Wertkontor-Lo.de</p>

    <div class="shop-button">Shop.Wertkontorlo.de</div>
  </div>
</body>
</html>
```